Financial e-service company needs a landing page

We need a landing page for a new start up Company.
We offer Electronic gift Cards.
We are using the primiraly the colours blue and white on our homepage. Our product is a new simple and serious financial payment way, so we need a landing page that gives a serious, professional and trustworthy look.
We are using normal browsers and would like the landing page to be scalable to different devices (tablet, phone).
In our topbar we have (se the uploaded files):
- The Company name = Solstrejfet.dk
- A home button = Hjem
- About Solstrejfet = Om Solstrejfet
- Contact us = kontakt os
- Redeem giftcard = indløs pengegave
- Sign me up = opret mig
- Log in botton = log på
At the center of the homepage we have different choice of giftcards solution as which the buyer can chose among.
- Print your personel giftcard (print selv)
- Electronic giftcard (elektronisk)
- Already have card (har kort)
I have attached our present logo - Solstrejfet by Silver Lark. There is a little story why the mother company is called Silver Lark instead of Money tree. It is because the company is started by three young guys.
Target Market(s)
Primiraly private individuals
Industry/Entity Type
Financial Service
Coding
Coded - Design and coding required
Number of Pages Required
1 page
Requirements
Must have
- - A top menu bar
- - a picture/drawning/figure (instead of the box - se screendump of homepage)
- - 3 different product choices - Print selv, Elektronisk and Har kort (se screendump homepage 1)
- - The prices of 3 different products (se screendump homepage 1)
Nice to have
- We have discused that maybe it would nice to have a log in box at the landing page, so it is for new users to sign up.
- We are open for other user minded suggestions

```html
<!DOCTYPE html>
<html lang="da">
<head>
<meta charset="utf-8">
<title>Solstrejfet</title>
<link href="https://fonts.googleapis.com/css2?family=Raleway:wght@400;500&family=Open+Sans:wght@400&display=swap" rel="stylesheet">
<style>
:root{
  --blue:#2b90cf;
  --navy:#0b3c94;
  --sky:#2f98d3;
  --orange:#f37d1e;
  --text:#3a3a3a;
  --muted:#555;
  --footer:#dcdcdc;
  --line:#cfcfcf;
}
*{margin:0;padding:0;box-sizing:border-box}
html,body{width:1200px;height:1133px;overflow:hidden;background:#fff}
body{position:relative;font-family:'Raleway',sans-serif;color:var(--text)}
.topbar{position:absolute;left:0;top:0;width:1200px;height:98px;background:#fff}
.brand{position:absolute;left:134px;top:32px;font-size:29px;font-weight:400;color:var(--blue);line-height:36px}
.nav{position:absolute;top:40px;font-size:15.5px;line-height:20px;color:#333;text-decoration:none}
.btn{position:absolute;top:31px;height:40px;line-height:40px;text-align:center;color:#fff;font-size:15px}
.btn-signup{left:870px;width:95px;background:var(--sky)}
.btn-login{left:972px;width:96px;background:var(--orange)}
.hero{position:absolute;left:0;top:98px;width:1200px;height:504px;
  background:linear-gradient(100deg,#a89a8c 0%,#8a7a6c 30%,#5d7fae 50%,#6f8fb8 65%,#a08b74 85%,#6e7a4a 100%)}
.hero-shade{position:absolute;inset:0;background:rgba(40,40,50,.25)}
.hero h1{position:absolute;left:0;width:1200px;top:172px;text-align:center;font-weight:400;font-size:40px;color:#fff;letter-spacing:.5px}
.hero p{position:absolute;left:0;width:1200px;text-align:center;font-size:22px;color:#fff}
.dots{position:absolute;left:555px;top:466px;display:flex;gap:4px}
.dot{width:18px;height:18px;border-radius:50%;background:#fff}
.dot.active{background:#222;border:3px solid #fff}
.card{position:absolute;top:687px;width:296px;height:242px;border:1px solid var(--line);
  background:linear-gradient(#fff 40%,#ececec)}
.card-icon{position:absolute;top:-64px;left:78px;width:140px;height:140px;border-radius:50%}
.card-icon svg{width:140px;height:140px}
.card h2{position:absolute;top:96px;width:100%;text-align:center;font-weight:400;font-size:24px;color:#333}
.card p{position:absolute;top:136px;width:100%;text-align:center;font-family:'Open Sans',sans-serif;font-size:12px;line-height:19px;color:var(--muted)}
.price{position:absolute;top:193px;width:100%;text-align:center;font-size:21px}
.footer{position:absolute;left:0;top:997px;width:1200px;height:136px;background:var(--footer)}
.flink{position:absolute;top:39px;font-size:16px;color:#666}
.copy{position:absolute;left:146px;top:72px;font-family:'Open Sans',sans-serif;font-size:12px;color:#666}
.social{position:absolute;top:32px;width:34px;height:34px;border-radius:50%;background:#fff}
</style>
</head>
<body>
<header class="topbar">
  <div class="brand">Solstrejfet</div>
  <a class="nav" style="left:389px">Hjem</a>
  <a class="nav" style="left:456px">Om Solstrejfet</a>
  <a class="nav" style="left:608px">kontakt os</a>
  <a class="nav" style="left:712px">indløs pengegave</a>
  <a class="btn btn-signup">opret mig</a>
  <a class="btn btn-login">log på</a>
</header>

<section class="hero" role="img" aria-label="Photo of a smiling couple on a sofa paying online with a card on a laptop">
  <div class="hero-shade"></div>
  <h1>WECLOME TO NORVA</h1>
  <p style="top:224px">At justo id velit placerat molestie Donec dictum lectus non odio</p>
  <p style="top:258px">Cras a ante vitae enim iaculis aliquam Mauris</p>
  <div class="dots"><span class="dot active"></span><span class="dot"></span><span class="dot"></span><span class="dot"></span></div>
</section>

<article class="card" style="left:135px">
  <div class="card-icon">
    <svg viewBox="0 0 140 140"><circle cx="70" cy="70" r="70" fill="var(--navy)"/><circle cx="70" cy="70" r="61" fill="none" stroke="#fff" stroke-opacity=".35"/>
      <g fill="none" stroke="#fff" stroke-width="5" stroke-linejoin="round"><rect x="44" y="38" width="48" height="14"/><rect x="38" y="52" width="64" height="28" rx="4"/><path d="M50 70h34v26l-8 8H50z"/><path d="M56 82h22M56 90h16"/></g></svg>
  </div>
  <h2>Print selv</h2>
  <p>Cras a ante vitae enim iaculis aliquam<br>Mauris nunc quam venenatis nec</p>
  <div class="price" style="color:var(--navy)">15 DDK</div>
</article>

<article class="card" style="left:450px">
  <div class="card-icon">
    <svg viewBox="0 0 140 140"><circle cx="70" cy="70" r="70" fill="var(--sky)"/><circle cx="70" cy="70" r="61" fill="none" stroke="#fff" stroke-opacity=".35"/>
      <g fill="none" stroke="#fff" stroke-width="4" stroke-linejoin="round"><rect x="42" y="48" width="58" height="42"/><path d="M42 48l29 24 29-24M42 90l21-21M100 90L79 69"/></g></svg>
  </div>
  <h2>Elektronisk</h2>
  <p>Cras a ante vitae enim iaculis aliquam<br>Mauris nunc quam venenatis nec</p>
  <div class="price" style="color:var(--sky)">25 DDK</div>
</article>

<article class="card" style="left:765px">
  <div class="card-icon">
    <svg viewBox="0 0 140 140"><circle cx="70" cy="70" r="70" fill="var(--orange)"/><circle cx="70" cy="70" r="61" fill="none" stroke="#fff" stroke-opacity=".35"/>
      <g fill="none" stroke="#fff" stroke-width="4" stroke-linejoin="round"><path d="M42 86V50l50-4 2 10"/><rect x="48" y="58" width="52" height="36" rx="3"/><path d="M48 66h52"/></g>
      <g fill="#fff"><rect x="54" y="72" width="24" height="5"/><rect x="82" y="72" width="12" height="8"/><rect x="54" y="82" width="10" height="4"/><rect x="67" y="82" width="10" height="4"/><rect x="80" y="84" width="14" height="4"/></g></svg>
  </div>
  <h2>Har kort</h2>
  <p>Cras a ante vitae enim iaculis aliquam<br>Mauris nunc quam venenatis nec</p>
  <div class="price" style="color:var(--orange)">10 DDK</div>
</article>

<footer class="footer">
  <a class="flink" style="left:146px">Home</a>
  <a class="flink" style="left:226px">About Us</a>
  <a class="flink" style="left:331px">Recruitment</a>
  <a class="flink" style="left:458px">Services</a>
  <a class="flink" style="left:558px">Blog</a>
  <a class="flink" style="left:628px">Contact</a>
  <div class="copy">© 2016 Company Name&nbsp; All right reserved</div>
  <span class="social" style="left:871px"></span>
  <span class="social" style="left:913px"></span>
  <span class="social" style="left:957px"></span>
  <span class="social" style="left:999px"></span>
</footer>
</body>
</html>
```